research new packaging for fresh rolls, plastic bag, no limit?

Family business: Manufacture and sale of different types of fresh bread since 1992 specializes in pita bread. This is a HANDMADE bread production company and FRESH delivered that morning. The plan is to release a new range of breads including: pita bread burger, hot dog bread, bagel, ... Our company wants a new model bag of bread, unfolded different type of bread FRESH in different colors. You have all seen radius sandwich bread in large area? I want better. I take the box of my father, made me prove that the future is already in place;) We look forward to you! Do not hesitate to contact us for more information. The joint "some ideas" and our logo.

Target Market(s)

We deliver grocers, and restaurants (food made or bistro). For grocers, target customers are young people, housewives, families.

Industry/Entity Type

Bakery

Font styles to use
Serif
Sans Serif
Decorative
Script

Requirements
Must have
• - Attached is our LOGO (.png) - Our brand must be easily identifiable. - That every kind of bread are recognizable by its color. (Example: red for sandwich bread, blue for pita bread ...). But the model of each bag is more or less the same. - (What are the age of the family business since 1992) - Bread FRESH, made in France, - Weight: 500g - Recipe idea - Nutrition facts - Contact: Website, Facebook, email, telephone, address = ° www. lmtbakery.example ° Lantern ° °contact@lmtbakery.example the fresh pita 0162839405 14 Rue des Tilleuls 93100 Montreuil printed bag all the way around, so spread the information. The bag should be about 40cm tall, 25 wide, the bellows would be 12cm "thickness". I foresee a bellows at the bottom of the bag for the package to stand up, and a bagger that will allow us to close the package with a ring where the date will be displayed.
Nice to have
• Same color for all our breads package. And a small color-coded to differentiate our kind of breads (eg www.corvinbakeries.example where the bag is almost the same and the difference is a small colorful acronym) No added coloring or flavoring Information to have on the bag A sandwich filled photo? Red? Like all bread existing brands? Our company is called "Lune-de-miel" we can find a connection? (Or not) (not mandatory)
Should not have
• To you tell me :)

```html
<!DOCTYPE html>
<html lang="en">
<head>
<meta charset="utf-8">
<title>Lune-de-miel Bakery – Pita Bread Bag</title>
<link rel="stylesheet" href="https://fonts.googleapis.com/css2?family=Comic+Neue:wght@400;700&display=swap">
<style>
  :root {
    --page: #ffffff;
    --bread-light: #ecdcc0;
    --bread-mid: #d9bd92;
    --bread-dark: #c49e6c;
    --band-red: #8e1a1e;
    --band-red-deep: #5c1012;
    --band-orange: #e8921e;
    --band-yellow: #f8e33c;
    --ink: #161008;
    --paper: #ffffff;
  }
  html, body {
    margin: 0;
    padding: 0;
    width: 1200px;
    height: 833px;
    overflow: hidden;
    background: var(--page);
  }
  .bag-face {
    display: block;
    width: 1200px;
    height: 833px;
  }
  .bag-face text {
    font-family: "Comic Neue", "Comic Sans MS", cursive;
  }
  .natural-claim { fill: var(--paper); font-size: 48px; }
  .variety-tab-label { fill: var(--paper); font-size: 24px; }
  .story-line { fill: var(--ink); font-size: 27px; font-weight: 700; }
  .since-mark { fill: var(--paper); font-size: 22px; }
  .brand-name { fill: var(--paper); font-size: 26px; font-weight: 700; }
  .brand-arc { fill: var(--paper); font-size: 16px; }
</style>
</head>
<body>
<svg class="bag-face" viewBox="0 0 1200 833" xmlns="http://www.w3.org/2000/svg">
  <defs>
    <linearGradient id="bread-fill" x1="0" y1="0" x2="0" y2="1">
      <stop offset="0" stop-color="var(--bread-mid)"/>
      <stop offset="0.5" stop-color="var(--bread-light)"/>
      <stop offset="1" stop-color="var(--bread-dark)"/>
    </linearGradient>
    <radialGradient id="red-fill" cx="0.45" cy="0.5" r="0.7">
      <stop offset="0" stop-color="var(--band-red-deep)"/>
      <stop offset="1" stop-color="var(--band-red)"/>
    </radialGradient>
    <radialGradient id="orange-fill" cx="0.5" cy="0.5" r="0.65">
      <stop offset="0" stop-color="var(--band-yellow)"/>
      <stop offset="1" stop-color="var(--band-orange)"/>
    </radialGradient>
    <path id="brand-arc-path" d="M872,318 Q970,430 872,545"/>
  </defs>

  <!-- bag body with bread seen through the film -->
  <g role="img" aria-label="Sliced pita bread seen through the clear bag">
    <path d="M228,300 Q228,228 300,228 L940,228 Q978,228 978,266 L978,630 L228,630 Z" fill="url(#bread-fill)"/>
  </g>

  <!-- centre orange band -->
  <rect class="centre-band" x="438" y="228" width="342" height="402" fill="url(#orange-fill)"/>

  <!-- left red panel -->
  <rect class="claim-panel" x="228" y="286" width="270" height="344" fill="url(#red-fill)"/>
  <text class="natural-claim" transform="translate(424,314) rotate(90)">Natural 100%</text>

  <!-- variety tab -->
  <rect class="variety-tab" x="490" y="348" width="46" height="182" rx="16" fill="var(--band-red)"/>
  <text class="variety-tab-label" transform="translate(505,376) rotate(90)">Pita Bread</text>

  <!-- story lines -->
  <g class="story" transform="rotate(90)">
    <text class="story-line" x="240" y="-654">Different Types of Fresh Bread</text>
    <text class="story-line" x="246" y="-618">Since 1992 Specializes In</text>
    <text class="story-line" x="340" y="-582">Pita Bread</text>
  </g>

  <!-- right red brand panel -->
  <rect class="brand-panel" x="730" y="286" width="248" height="290" fill="url(#red-fill)"/>
  <text class="since-mark" transform="translate(744,384) rotate(90)">Since 1992</text>

  <g class="brand" transform="translate(836,438) rotate(90)">
    <circle cx="-86" cy="-8" r="7" fill="var(--paper)"/>
    <text class="brand-name" x="0" y="-8" text-anchor="middle">Lune-de-miel</text>
    <text class="brand-name" x="0" y="22" text-anchor="middle">Bakery</text>
  </g>

  <text class="brand-arc"><textPath href="#brand-arc-path" startOffset="50%" text-anchor="middle">Different Types of Fresh Bread</textPath></text>
</svg>
</body>
</html>
```